Website home page

www.quvanti.com - a website for traditional real estate and real Estate Auctions
We need a home page.
Please disregard the colors quvanti.com is designed with. Choose any colors you have in mind. Surprise us.
Home page should have the following buttons on it:
About Me
My Listings
Property Search
Buyers/Sellers
Concierge
Contact Me

Try buttons with pictures or without pictures, again, surprise us.
The page should not display property listings.
You can use property pictures - exterior and/or interior, nature or landscape pictures as an enhancement of the page. (if it will be the case)
Themes suggestions:
-modern
-hi-tech
-elegant
surprise us
Some sites that we like:
http://www.findlamberdell.com/
http://www.homesteadmarvick.com/
http://www.trivanpeak.com/
http://www.gildedhavenestates.com/
http://www.fennickpartners.com/

Target Market(s)

Home buyers and sellers

Industry/Entity Type

Real Estate

Requirements
Must have
• Home page should have the following buttons on it:
About Me
My Listings
Property Search
Buyers/Sellers
Concierge
Contact Me

```html
<!DOCTYPE html>
<html lang="en">
<head>
<meta charset="utf-8">
<title>Quvanti — Home</title>
<link rel="stylesheet" href="https://fonts.googleapis.com/css2?family=Marcellus&family=Marcellus+SC&display=swap">
<style>
  :root {
    --bg: #000000;
    --gold: #edb96a;
    --gold-deep: #c8954a;
    --rule: #6b5634;
    --rule-grey: #4a4a4a;
    --text: #ffffff;
    --muted: #5c5c5c;
    --dot: #f1c27a;
  }
  * { margin: 0; padding: 0; box-sizing: border-box; }
  html, body { width: 1200px; height: 841px; overflow: hidden; background: var(--bg); }
  .page { position: relative; width: 1200px; height: 841px; background: var(--bg); }

  .brand {
    position: absolute; top: 22px; left: 0; width: 1200px; text-align: center;
    font-family: "Marcellus", serif; font-size: 42px; color: var(--gold-deep);
    line-height: 52px; letter-spacing: 1px;
  }

  .main-nav {
    position: absolute; top: 95px; left: 143px; width: 914px;
    display: flex; justify-content: space-between;
    font-family: "Marcellus", serif; font-size: 14px; color: var(--gold);
    letter-spacing: 0.4px; text-transform: uppercase;
  }
  .main-nav a { color: inherit; text-decoration: none; }
  .nav-rule { position: absolute; top: 128px; left: 143px; width: 914px; height: 1px; background: var(--rule); }

  .slide { position: absolute; border: 1px solid var(--gold-deep); }
  .slide-side-left {
    left: 143px; top: 355px; width: 162px; height: 147px;
    background: linear-gradient(180deg, #6aa9c9 0%, #9fc7d2 30%, #8a8a80 55%, #e9e6dc 80%, #3d64a6 100%);
  }
  .slide-main {
    left: 304px; top: 169px; width: 593px; height: 363px;
    background: linear-gradient(160deg, #2f8ee0 0%, #5aa6e8 25%, #b36b55 45%, #8e5646 65%, #4f7a32 85%, #6e9b3c 100%);
  }
  .slide-side-right {
    left: 896px; top: 355px; width: 162px; height: 147px;
    background: linear-gradient(180deg, #2a3a78 0%, #c9b6a8 40%, #e2c99a 70%, #8a6a44 100%);
  }

  .slider-bar-top { position: absolute; top: 545px; left: 274px; width: 652px; height: 1px; background: var(--rule); }
  .slider-bar-bottom { position: absolute; top: 565px; left: 274px; width: 652px; height: 1px; background: var(--rule-grey); }
  .slider-dots { position: absolute; top: 550px; left: 528px; display: flex; gap: 9px; }
  .slider-dots span { width: 10px; height: 10px; border-radius: 50%; border: 1px solid var(--dot); }
  .slider-dots span.is-active { background: var(--dot); }

  .welcome { position: absolute; top: 598px; left: 143px; width: 914px; }
  .welcome h1 {
    font-family: "Marcellus SC", serif; font-weight: 400; font-size: 24px;
    color: var(--gold); line-height: 30px; margin-bottom: 7px;
  }
  .welcome p {
    font-family: Arial, Helvetica, sans-serif; font-size: 13.4px; line-height: 21px; color: var(--text);
  }
  .welcome p a { color: var(--gold); font-weight: bold; text-decoration: none; }

  .footer-rule { position: absolute; top: 760px; left: 143px; width: 914px; height: 1px; background: var(--rule); }
  .contact-line {
    position: absolute; top: 775px; left: 0; width: 1200px; text-align: center;
    font-family: "Marcellus", serif; font-size: 13px; color: var(--gold);
  }
  .contact-line .sep { display: inline-block; margin: 0 9px; font-size: 10px; vertical-align: 1px; }

  .share-row { position: absolute; top: 798px; left: 501px; display: flex; gap: 12px; }
  .share { display: flex; align-items: center; gap: 3px; }
  .share .chip { width: 32px; height: 14px; background: #d9dde6; border-radius: 2px; }
  .share .count {
    font-family: Arial, sans-serif; font-size: 9px; color: #333; background: #fff;
    border: 1px solid #bbb; height: 14px; line-height: 12px; padding: 0 2px;
  }
  .share-small .chip { width: 22px; }

  .copyright {
    position: absolute; top: 811px; right: 142px;
    font-family: "Marcellus", serif; font-size: 10px; color: var(--muted);
  }
</style>
</head>
<body>
<div class="page">
  <header>
    <div class="brand">Quvanti</div>
    <nav class="main-nav">
      <a href="#">About Me</a>
      <a href="#">My Listings</a>
      <a href="#">Property Search</a>
      <a href="#">Buyers / Sellers</a>
      <a href="#">Concierge</a>
      <a href="#">Contact Me</a>
    </nav>
    <div class="nav-rule"></div>
  </header>

  <section class="slider">
    <div class="slide slide-side-left" role="img" aria-label="Beach resort with thatched umbrellas and loungers by turquoise sea"></div>
    <div class="slide slide-side-right" role="img" aria-label="White villa courtyard lit warmly at dusk"></div>
    <div class="slide slide-main" role="img" aria-label="Historic red sandstone mansion with wraparound porch under blue sky"></div>
    <div class="slider-bar-top"></div>
    <div class="slider-dots">
      <span class="is-active"></span><span></span><span></span><span></span><span></span><span></span><span></span><span></span>
    </div>
    <div class="slider-bar-bottom"></div>
  </section>

  <section class="welcome">
    <h1>Welcome to Quvanti</h1>
    <p>Lorem ipsum dolor sit amet, consectetur adipiscing elit. Cras non felis eu nisi pellentesque eleifend eget pharetra sapien. Etiam et risus nec leo elementum pulvinar sollicitudin eu diam. Aenean mauris erat, gravida et pellentesque ut, sollicitudin sit amet mi. Suspendisse sem nulla, semper in vehicula id, accums an eu turpis. Quisque interdum magna risus, sit amet vestibulum ante. Proin vel risus sed nisi tristique ornare. Sed vulputate varius nulla, in rhoncus estsu scipit imperdiet. Mauris vulputate hendrerit metus, eget sagittis risus molestie nec enean tempus juio elle. For more information, please <a href="#">contact us</a>.</p>
  </section>

  <footer>
    <div class="footer-rule"></div>
    <div class="contact-line">42 Willow Ridge Court Suite 210, Marvale, CA 94017<span class="sep">&#9679;</span>888.555.0142<span class="sep">&#9679;</span>support@quvanti.com</div>
    <div class="share-row">
      <div class="share"><span class="chip"></span><span class="count">1212</span></div>
      <div class="share"><span class="chip"></span><span class="count">444</span></div>
      <div class="share share-small"><span class="chip"></span><span class="count">102</span></div>
    </div>
    <div class="copyright">&copy;2012 Quvanti. All Rights Reserved.</div>
  </footer>
</div>
</body>
</html>
```